Anzeigengestaltung für Produzent von geschälten und gegarten Kartoffeln
Zielgruppe
Wir produzieren geschälte und gegarte Kartoffel. Unsere Zielgruppe ist hauptsächlich der Gastronomiegroßhandel. Die Anzeige im speziellen soll die Gastronomen ansprechen (zB auch durch Fotos von zubereiteten Erdäpfeln)
Aufgabenstellung
Das DIN Format ist vorgegeben: 1/2 Seite quer - 225 x 146mm (+3mm Überfüller).
Die Anzeige soll die Gastronomen/Köche ansprechen, unser Produkt zu kaufen. Wir verwenden bei unseren Produkten keine Konservierungsmittel, das möchten wir speziell hervorheben. In Österreich hat das ÖPV-Gütesiegel einen sehr hohen Stellenwert. Daher soll auch dieses auf der Anzeige zu sehen sein. Unser Logo soll natürlich auch in die Anzeige.
Die Anzeige wird in einem Magazin geschalten, in dem auch ein Bericht über unseren Betrieb abgedruckt wird. Daher brauchen wir nicht viel Text. Die Anzeige soll Lust bzw. Appetit auf Kartoffelgerichte machen. Bitte keine Pommes!

```html
<!DOCTYPE html>
<html lang="de">
<head>
<meta charset="utf-8">
<title>Die Knollerei – Anzeige</title>
<link rel="stylesheet" href="https://fonts.googleapis.com/css2?family=Delius&family=Open+Sans:wght@600;700&display=swap">
<style>
  :root {
    --green: #4b9a2f;
    --green-badge: #4f9a33;
    --band: #4a3e12;
    --gold: #c9a322;
    --logo-gold: #d4b01e;
    --white: #ffffff;
    --seal-grey: #d9d6cc;
    --dark: #1b1a16;
  }
  * { margin: 0; padding: 0; box-sizing: border-box; }
  html, body { width: 1200px; height: 778px; overflow: hidden; background: var(--dark); }
  .ad {
    position: relative;
    width: 1200px;
    height: 778px;
    overflow: hidden;
    font-family: "Open Sans", sans-serif;
  }
  .hero-photo {
    position: absolute;
    left: 0; top: 0;
    width: 1200px; height: 662px;
    background:
      radial-gradient(ellipse 330px 230px at 820px 420px, #f0c640 0%, #e0a92a 45%, rgba(120,85,20,0.6) 75%, rgba(0,0,0,0) 100%),
      radial-gradient(ellipse 520px 330px at 830px 430px, #3a3a36 0%, #232320 70%, rgba(0,0,0,0) 100%),
      linear-gradient(100deg, #191813 0%, #2a2a24 45%, #2e2d28 70%, #1f1e1a 100%);
  }
  .brand {
    position: absolute;
    left: 40px; top: 78px;
    color: var(--logo-gold);
    font-weight: 700;
    font-size: 57px;
    line-height: 1.05;
    text-transform: uppercase;
  }
  .headline { position: absolute; left: 0; top: 0; font-weight: 400; }
  .headline-line {
    position: absolute;
    background: var(--green);
    color: var(--white);
    font-family: "Delius", sans-serif;
    font-size: 70px;
    line-height: 1;
    display: flex;
    align-items: center;
    justify-content: center;
  }
  .line-1 { left: 41px;  top: 264px; width: 252px; height: 90px; }
  .line-2 { left: 83px;  top: 354px; width: 355px; height: 93px; }
  .line-3 { left: 131px; top: 447px; width: 162px; height: 88px; }
  .line-4 { left: 41px;  top: 535px; width: 379px; height: 90px; }
  .claim-badge {
    position: absolute;
    left: 980px; top: 42px;
    width: 172px; height: 172px;
    border-radius: 50%;
    background: var(--green-badge);
    color: var(--white);
    font-weight: 600;
    font-size: 21px;
    line-height: 1.25;
    text-align: center;
    display: flex;
    align-items: center;
    justify-content: center;
    transform: rotate(3deg);
  }
  .footer-band {
    position: absolute;
    left: 0; top: 662px;
    width: 1200px; height: 116px;
    background: var(--band);
  }
  .tagline, .web {
    position: absolute;
    top: 707px;
    color: var(--gold);
    font-weight: 600;
    font-size: 20px;
    line-height: 1.3;
  }
  .tagline { left: 41px; }
  .web { left: 743px; }
  .quality-seal {
    position: absolute;
    left: 1023px; top: 673px;
    width: 166px; height: 95px;
    background: var(--white);
    border-radius: 14px;
    display: flex;
    align-items: center;
    justify-content: center;
  }
  .quality-seal-shape {
    width: 70px; height: 70px;
    border-radius: 50%;
    background: var(--seal-grey);
  }
</style>
</head>
<body>
  <div class="ad">
    <div class="hero-photo" role="img" aria-label="Foto: gebratene goldgelbe Erdäpfel mit frischer Petersilie in einer dunklen Schale"></div>

    <div class="brand">Die<br>Knollerei</div>

    <h1 class="headline">
      <span class="headline-line line-1">Wenig</span>
      <span class="headline-line line-2">Aufwand</span>
      <span class="headline-line line-3">viel</span>
      <span class="headline-line line-4">Geschmack</span>
    </h1>

    <div class="claim-badge">Ohne<br>Konservie-<br>rungsmittel</div>

    <div class="footer-band"></div>
    <p class="tagline">Ihr Spezialist für geschälte Erdäpfel</p>
    <p class="web">www.knollerei.at</p>

    <div class="quality-seal" role="img" aria-label="Platz für das ÖPV-Gütesiegel">
      <div class="quality-seal-shape"></div>
    </div>
  </div>
</body>
</html>
```